I need 4 Power Point foils for 4 companies.
1 Folis for Tovanta, 1 Foils for Luxury, 1 Folis for Hospitality Group and the mother of Tovan and Luxury is Hospitality. So we also need a foil as head hospitality and you have to realize that the other companies belong to it. I would like a cover sheet and a presentation templates.
Updates
Hey i Need for My companies Presentation Cover and Template thank you
Target Market(s)
Travel industry
Colors
Designer to choose only greyscale colors for use in the design.
Requirements
Must have
- create your own design

```html
<!DOCTYPE html>
<html lang="en">
<head>
<meta charset="utf-8">
<title>Halvern Group – Presentation Covers and Template</title>
<link href="https://fonts.googleapis.com/css2?family=Roboto:wght@300;400;500;700;900&display=swap" rel="stylesheet">
<style>
:root{
  --canvas:#a9a9a9;
  --ink:#1b1b1b;
  --dark:#262626;
  --mid:#8a8a8a;
  --soft:#c4c4c4;
  --light:#f1f1f1;
  --line:#dcdcdc;
  --text:#5a5a5a;
  --blue:#3a6cf4;
  --white:#ffffff;
}
*{box-sizing:border-box;margin:0;padding:0}
html,body{width:703px;height:1200px;overflow:hidden}
body{background:var(--canvas);font-family:'Roboto',sans-serif;color:var(--ink)}
.deck{position:relative;width:703px;height:1200px}
.slide{position:absolute;width:227px;height:128px;background:var(--white);overflow:hidden}
.c1{left:6px}.c2{left:238px}.c3{left:470px}
.r1{top:6px}.r2{top:138px}.r3{top:271px}.r4{top:404px}.r5{top:536px}.r6{top:668px}.r7{top:801px}.r8{top:933px}.r9{top:1066px}
.abs{position:absolute}
.photo{position:absolute}

/* brand marks */
.mark{position:absolute;border-radius:50%;background:var(--white);display:flex;align-items:center;justify-content:center;text-align:center;font-weight:700;color:var(--ink);line-height:1.05;box-shadow:0 1px 4px rgba(0,0,0,.25)}
.mark.dark{background:var(--dark);color:var(--white)}

/* side rail */
.rail-mark{position:absolute;left:3px;top:7px;width:9px;height:9px;border-radius:50%;border:.5px solid var(--soft);background:var(--white);font-size:1.5px;font-weight:700;display:flex;align-items:center;justify-content:center}
.rail-line{position:absolute;left:12px;top:4px;bottom:4px;width:.5px;background:var(--line)}
.rail-copy{position:absolute;left:-14px;top:62px;width:40px;font-size:1.7px;color:var(--mid);transform:rotate(-90deg);text-align:center;white-space:nowrap}
.rail-page{position:absolute;left:3px;bottom:5px;width:7px;height:7px;border-radius:50%;background:var(--light);font-size:1.8px;display:flex;align-items:center;justify-content:center;color:var(--text)}

/* cover type */
.cover-title{position:absolute;font-weight:900;line-height:.98;letter-spacing:.1px}
.cover-sub{position:absolute;font-weight:300}
.btn{position:absolute;height:9px;border-radius:5px;background:var(--blue);color:var(--white);font-size:2.8px;font-weight:700;display:flex;align-items:center;justify-content:center;letter-spacing:.1px}
.bar{position:absolute;left:0;right:0;background:var(--dark)}

/* section headings */
.h-title{position:absolute;left:0;right:0;top:12px;text-align:center;font-size:9.6px;font-weight:500}
.h-sub{position:absolute;left:0;right:0;top:23px;text-align:center;font-size:2.2px;letter-spacing:.9px;color:var(--text)}
.h-rule{position:absolute;left:108px;top:27px;width:11px;height:1px;background:var(--mid)}
.copy{font-size:2.5px;line-height:1.45;color:var(--text)}
.label{font-size:3.4px;font-weight:700;color:var(--ink)}
.pic{position:absolute;background:var(--light);display:flex;align-items:center;justify-content:center;font-size:3.2px;color:var(--text)}
.icon-dot{position:absolute;width:11px;height:11px;border-radius:50%;background:var(--mid);border:1.5px solid var(--line)}

/* agenda */
.agenda-row{position:absolute;left:73px;width:115px;height:9px;border-bottom:.5px dashed var(--line);display:flex;align-items:center;font-size:3.8px}
.agenda-row b{width:27px;font-weight:700}
.agenda-row span{color:var(--mid)}

/* table */
.grid-table{position:absolute;border-collapse:collapse;font-size:2.6px;text-align:center}
.grid-table td,.grid-table th{height:8px;border-bottom:.5px solid var(--line)}
.grid-table th{font-weight:700;border-bottom:1px solid var(--mid);border-top:1px solid var(--mid)}
.grid-table tr.hl td{background:var(--blue);color:var(--white)}

.tag{position:absolute;background:var(--blue);color:var(--white);font-size:2.2px;font-weight:700;padding:.6px 3px}
.tag-copy{position:absolute;font-size:1.9px;line-height:1.4;color:var(--text);width:26px}
</style>
</head>
<body>
<main class="deck">

<!-- 1 photo cover -->
<section class="slide c1 r1">
  <div class="photo" role="img" aria-label="Warm hotel lobby interior" style="inset:0;background:linear-gradient(135deg,#2f241b,#5e432b 55%,#8a6b48)"></div>
  <svg class="abs" style="left:0;top:0" width="227" height="128" viewBox="0 0 227 128"><path d="M0 128 L0 118 Q130 115 227 38 L227 128 Z" fill="#fff"/></svg>
  <div class="photo" role="img" aria-label="Hotel bar with guests" style="left:131px;top:21px;width:70px;height:70px;border-radius:50%;border:3px solid #fff;background:radial-gradient(circle at 40% 40%,#d9a871,#7a5134 60%,#3a6a66);box-shadow:0 2px 6px rgba(0,0,0,.3)"></div>
  <div class="cover-title" style="left:17px;top:34px;font-size:13.5px;color:#fff">TITLE OF<br>PRESENTATION</div>
  <div class="cover-sub" style="left:17px;top:64px;font-size:5.5px;color:#fff">Here Goes A Short Subtitle</div>
  <div class="btn" style="left:17px;top:88px;width:42px">PRESENTER NAME</div>
  <div class="mark" style="left:198px;top:99px;width:22px;height:22px;font-size:2.6px">Halvern</div>
  <div class="mark dark" style="left:168px;top:117px;width:7px;height:7px;font-size:1.3px">Lumora</div>
  <div class="mark" style="left:183px;top:113px;width:10px;height:10px;font-size:1.5px">Tovanta</div>
</section>

<!-- 2 dark cover -->
<section class="slide c2 r1" style="background:var(--dark)">
  <svg class="abs" style="left:0;top:0" width="227" height="128" viewBox="0 0 227 128"><path d="M166 0 Q148 40 176 72 Q200 100 184 128 L227 128 L227 0 Z" fill="#fff"/></svg>
  <div class="cover-title" style="left:12px;top:44px;font-size:14px;color:#fff">TITLE OF<br>PRESENTATION</div>
  <div class="cover-sub" style="left:12px;top:73px;font-size:6px;color:#fff">Here Goes A Short Subtitle</div>
  <div class="btn" style="left:12px;top:99px;width:42px">PRESENTER NAME</div>
  <div class="mark" style="left:138px;top:34px;width:38px;height:38px;font-size:4px;border:1.5px solid var(--dark)">Halvern<br>Group</div>
  <div class="mark" style="left:114px;top:4px;width:17px;height:17px;font-size:2.4px">Tovanta</div>
  <div class="mark dark" style="left:157px;top:97px;width:17px;height:17px;font-size:2.4px;border:1px solid #fff">Lumora</div>
</section>

<!-- 3 group cover -->
<section class="slide c3 r1">
  <div class="bar" style="top:0;height:2px"></div>
  <div class="abs" style="left:150px;top:14px;width:70px;height:70px;border-radius:50%;border:3px solid #eef0f3"></div>
  <div class="mark" style="left:104px;top:12px;width:22px;height:22px;font-size:2.8px">Halvern</div>
  <div class="cover-title" style="left:0;right:0;top:46px;text-align:center;font-size:17px">TITLE OF<br>PRESENTATION</div>
  <div class="cover-sub" style="left:0;right:0;top:82px;text-align:center;font-size:7px">Here Goes A Short Subtitle</div>
  <div class="btn" style="left:90px;top:102px;width:42px">PRESENTER NAME</div>
  <div class="bar" style="bottom:0;height:3px"></div>
</section>

<!-- 4 Tovanta cover -->
<section class="slide c1 r2">
  <div class="bar" style="top:0;height:2px"></div>
  <div class="abs" style="left:100px;top:30px;width:80px;height:80px;border-radius:50%;background:radial-gradient(circle,#f5eef4,#fff 70%)"></div>
  <div class="mark" style="left:98px;top:8px;width:28px;height:28px;font-size:3.4px">Tovanta</div>
  <div class="cover-title" style="left:0;right:0;top:46px;text-align:center;font-size:17px">TITLE OF<br>PRESENTATION</div>
  <div class="cover-sub" style="left:0;right:0;top:82px;text-align:center;font-size:7px">Here Goes A Short Subtitle</div>
  <div class="btn" style="left:90px;top:102px;width:42px">PRESENTER NAME</div>
  <div class="bar" style="bottom:0;height:3px"></div>
</section>

<!-- 5 Lumora cover -->
<section class="slide c2 r2">
  <div class="bar" style="top:0;height:2px"></div>
  <div class="abs" style="left:105px;top:24px;width:80px;height:80px;border-radius:50%;background:radial-gradient(circle,#f7f3ea,#fff 70%)"></div>
  <div class="mark dark" style="left:101px;top:11px;width:24px;height:24px;font-size:3px">Lumora</div>
  <div class="cover-title" style="left:0;right:0;top:46px;text-align:center;font-size:17px">TITLE OF<br>PRESENTATION</div>
  <div class="cover-sub" style="left:0;right:0;top:82px;text-align:center;font-size:7px">Here Goes A Short Subtitle</div>
  <div class="btn" style="left:90px;top:102px;width:42px">PRESENTER NAME</div>
  <div class="bar" style="bottom:0;height:3px"></div>
</section>

<!-- 6 agenda -->
<section class="slide c3 r2">
  <div class="photo" role="img" aria-label="Dark evening landscape" style="left:0;top:0;width:90px;height:128px;background:linear-gradient(180deg,#2b2b2b,#1e1e1e)"></div>
  <div class="abs" style="left:16px;top:56px;font-size:12px;font-weight:500;color:#fff">Agenda</div>
  <div class="agenda-row" style="top:32px"><b>01</b><span>Introduction - Welcome</span></div>
  <div class="agenda-row" style="top:41px"><b>02</b><span>Mission &amp; Vision</span></div>
  <div class="agenda-row" style="top:50px"><b>03</b><span>Our Services</span></div>
  <div class="agenda-row" style="top:59px"><b>04</b><span>Company Profile</span></div>
  <div class="agenda-row" style="top:68px"><b>05</b><span>Company Profile</span></div>
  <div class="agenda-row" style="top:77px"><b>06</b><span>Our Team</span></div>
  <div class="agenda-row" style="top:86px"><b>07</b><span>Our Offices</span></div>
  <div class="agenda-row" style="top:95px"><b>08</b><span>Q&amp;As / Closing Speech</span></div>
</section>

<!-- 7-9 divider slides -->
<section class="slide c1 r3">
  <span class="rail-mark">Tovanta</span><span class="rail-line"></span><span class="rail-copy">Copyright © | All Rights Reserved</span><span class="rail-page">7</span>
  <div class="abs" style="left:118px;top:15px;width:98px;height:98px;border-radius:50%;border:3px solid #ececec;display:flex;align-items:center;justify-content:center;font-size:11px;font-weight:700;color:#e4e4e4">Tovanta</div>
</section>
<section class="slide c2 r3">
  <span class="rail-mark">Halvern</span><span class="rail-line"></span><span class="rail-copy">Copyright © | All Rights Reserved</span><span class="rail-page">8</span>
  <div class="abs" style="left:116px;top:14px;width:100px;height:100px;border-radius:50%;border:3px solid #e8ecf1;display:flex;align-items:center;justify-content:center;font-size:11px;font-weight:700;color:#e1e6ed">Halvern</div>
</section>
<section class="slide c3 r3">
  <span class="rail-mark">Lumora</span><span class="rail-line"></span><span class="rail-copy">Copyright © | All Rights Reserved</span><span class="rail-page">9</span>
  <div class="abs" style="left:114px;top:15px;width:98px;height:98px;border-radius:50%;background:#eeeeee;border:3px solid #f6f6f6;display:flex;align-items:center;justify-content:center;font-size:11px;font-weight:700;color:#e0dccf">Lumora</div>
</section>

<!-- 10 two-column text -->
<section class="slide c1 r4">
  <span class="rail-mark">Tovanta</span><span class="rail-line"></span><span class="rail-copy">Copyright © | All Rights Reserved</span><span class="rail-page">10</span>
  <div class="h-title">Here Add Your Awesome Title</div><div class="h-sub">WRITE HERE A GREAT SUBTITLE</div><div class="h-rule"></div>
  <div class="abs copy" style="left:22px;top:42px;width:90px">Lorem ipsum dolor sit amet, consectetur adipiscing elit, sed do eiusmod tempor incididunt ut labore et dolore magna aliqua. Ut enim ad minim veniam, quis nostrud exercitation ullamco laboris nisi ut aliquip ex ea commodo.<br><b>Lorem ipsum dolor sit amet, consectetur</b><br>• Sed do eiusmod tempor incididunt ut labore<br>• Dolore magna aliqua ut enim ad minim<br><b>Quis nostrud exercitation ullamco laboris</b><br>• Lorem ipsum dolor sit amet adipiscing<br>• Sed do eiusmod tempor incididunt ut labore<br><b>Lorem ipsum dolor sit amet, consectetur</b><br>• Dolore magna aliqua ut enim ad minim</div>
  <div class="abs copy" style="left:122px;top:42px;width:90px">Lorem ipsum dolor sit amet, consectetur adipiscing elit, sed do eiusmod tempor incididunt ut labore et dolore magna aliqua. Ut enim ad minim veniam, quis nostrud exercitation ullamco laboris nisi ut aliquip ex ea commodo.<br><b>Lorem ipsum dolor sit amet, consectetur</b><br>• Sed do eiusmod tempor incididunt ut labore<br>• Dolore magna aliqua ut enim ad minim<br><b>Quis nostrud exercitation ullamco laboris</b><br>• Lorem ipsum dolor sit amet adipiscing<br>• Sed do eiusmod tempor incididunt ut labore<br><b>Lorem ipsum dolor sit amet, consectetur</b><br>• Dolore magna aliqua ut enim ad minim</div>
</section>

<!-- 11 image and title -->
<section class="slide c2 r4">
  <div class="photo" role="img" aria-label="Open suitcase with hat and travel items" style="left:0;top:0;width:96px;height:128px;border-radius:0 64px 64px 0;background:linear-gradient(160deg,#3f5a44,#d8d8d4 45%,#5a5a5a)"></div>
  <div class="mark" style="left:79px;top:21px;width:19px;height:19px;font-size:2.4px">Tovanta</div>
  <div class="abs" style="left:108px;top:30px;font-size:9px;font-weight:500;line-height:1.2">Here Goes<br>Title Of This Slide</div>
  <div class="abs copy" style="left:108px;top:59px;width:104px">Lorem ipsum dolor sit amet, consectetur adipiscing elit, sed do eiusmod tempor incididunt ut labore et dolore magna aliqua. Lorem ipsum dolor sit amet, consectetur adipiscing elit, sed do eiusmod tempor incididunt ut labore et dolore magna aliqua. Ut enim ad minim veniam, quis nostrud exercitation ullamco laboris nisi ut aliquip.<br><br>Lorem ipsum dolor sit amet, consectetur adipiscing elit, sed do eiusmod tempor incididunt ut labore et dolore magna aliqua. Lorem ipsum dolor sit amet, sed do eiusmod tempor incididunt ut labore.</div>
</section>

<!-- 12 six items -->
<section class="slide c3 r4">
  <span class="rail-mark">Tovanta</span><span class="rail-line"></span><span class="rail-copy">Copyright © | All Rights Reserved</span><span class="rail-page"></span>
  <div class="h-title">Here Add Your Awesome Title</div><div class="h-sub">WRITE HERE A GREAT SUBTITLE</div><div class="h-rule"></div>
  <span class="icon-dot" style="left:27px;top:44px"></span><span class="icon-dot" style="left:27px;top:68px"></span><span class="icon-dot" style="left:27px;top:92px"></span>
  <span class="icon-dot" style="left:125px;top:44px"></span><span class="icon-dot" style="left:125px;top:68px"></span><span class="icon-dot" style="left:125px;top:92px"></span>
  <div class="abs" style="left:45px;top:41px;width:60px"><div class="label">Project name</div><div class="copy">Lorem ipsum dolor sit amet, nec an dictas equidem appellantur, ut has commune accommodare.</div></div>
  <div class="abs" style="left:45px;top:65px;width:60px"><div class="label">Project name</div><div class="copy">Lorem ipsum dolor sit amet, nec an dictas equidem appellantur, ut has commune accommodare.</div></div>
  <div class="abs" style="left:45px;top:89px;width:60px"><div class="label">Project name</div><div class="copy">Lorem ipsum dolor sit amet, nec an dictas equidem appellantur, ut has commune accommodare.</div></div>
  <div class="abs" style="left:143px;top:41px;width:60px"><div class="label">Project name</div><div class="copy">Lorem ipsum dolor sit amet, nec an dictas equidem appellantur, ut has commune accommodare.</div></div>
  <div class="abs" style="left:143px;top:65px;width:60px"><div class="label">Project name</div><div class="copy">Lorem ipsum dolor sit amet, nec an dictas equidem appellantur, ut has commune accommodare.</div></div>
  <div class="abs" style="left:143px;top:89px;width:60px"><div class="label">Project name</div><div class="copy">Lorem ipsum dolor sit amet, nec an dictas equidem appellantur, ut has commune accommodare.</div></div>
</section>

<!-- 13 quote with photo -->
<section class="slide c1 r5">
  <span class="rail-mark">Tovanta</span><span class="rail-line"></span><span class="rail-copy">Copyright © | All Rights Reserved</span><span class="rail-page">13</span>
  <div class="photo" role="img" aria-label="Traveller sitting by a mountain lake" style="left:12px;top:0;width:100px;height:128px;background:linear-gradient(180deg,#9aa7a6,#4f7a7e 45%,#2b4247)"></div>
  <div class="abs" style="left:120px;top:34px;width:12px;height:.8px;background:var(--mid)"></div>
  <div class="abs" style="left:120px;top:37px;width:100px;font-size:5.8px;font-weight:700;line-height:1.08">Success is not only what you achieve in your life, but also what you inspire in the lives of others</div>
  <div class="abs" style="left:52px;top:84px;width:175px;height:44px;border-radius:9px 0 0 0;background:linear-gradient(90deg,#7c7c7c,#b8b8b8)"></div>
  <div class="abs" style="left:66px;top:96px;width:45px;color:#fff"><div style="font-size:3.2px;font-weight:700">Lorem ipsum dolor</div><div style="font-size:2.4px;line-height:1.4;margin-top:2px">Lorem ipsum dolor sit amet, consectetur adipiscing elit, sed do eiusmod</div></div>
  <div class="abs" style="left:120px;top:96px;width:45px;color:#fff"><div style="font-size:3.2px;font-weight:700">Lorem ipsum dolor</div><div style="font-size:2.4px;line-height:1.4;margin-top:2px">Lorem ipsum dolor sit amet, consectetur adipiscing elit, sed do eiusmod</div></div>
  <div class="abs" style="left:176px;top:96px;width:45px;color:#fff"><div style="font-size:3.2px;font-weight:700">Lorem ipsum dolor</div><div style="font-size:2.4px;line-height:1.4;margin-top:2px">Lorem ipsum dolor sit amet, consectetur adipiscing elit, sed do eiusmod</div></div>
</section>

<!-- 14 text and pic -->
<section class="slide c2 r5">
  <span class="rail-mark">Tovanta</span><span class="rail-line"></span><span class="rail-copy">Copyright © | All Rights Reserved</span><span class="rail-page">14</span>
  <div class="abs" style="left:20px;top:24px;font-size:10.5px;font-weight:500">Text and Pic</div>
  <div class="abs" style="left:21px;top:37px;font-size:2.2px;letter-spacing:.9px;color:var(--text)">WRITE HERE A GREAT SUBTITLE</div>
  <div class="abs copy" style="left:21px;top:51px;width:72px">Lorem ipsum dolor sit amet, consectetur adipiscing elit, sed do eiusmod tempor incididunt ut labore et dolore magna aliqua. Ut enim ad minim veniam, quis nostrud exercitation ullamco laboris nisi ut aliquip ex. Lorem ipsum dolor sit amet, consectetur adipiscing elit, sed do eiusmod tempor incididunt ut labore et dolore magna aliqua.</div>
  <div class="btn" style="left:19px;top:104px;width:40px">Your Text Here</div>
  <div class="pic" style="left:107px;top:18px;width:40px;height:45px">Picture Here</div>
  <div class="abs" style="left:148px;top:18px;width:70px;height:45px;background:linear-gradient(135deg,#777,#a9a9a9);padding:5px 7px;color:#fff"><div style="font-size:3px;font-weight:700">Project name</div><div style="font-size:2.2px;line-height:1.4;margin-top:2px">Lorem ipsum dolor sit amet, nec an dictas equidem appellantur, ut has commune accommodare. Mea illum, ludus solet idpro.</div></div>
  <div class="abs" style="left:107px;top:66px;width:73px;height:46px;background:linear-gradient(135deg,#777,#a9a9a9);padding:7px 8px;color:#fff"><div style="font-size:3px;font-weight:700">Project name</div><div style="font-size:2.2px;line-height:1.4;margin-top:2px">Lorem ipsum dolor sit amet, nec an dictas equidem appellantur, ut has commune accommodare. Mea illum, ludus solet idpro.</div></div>
  <div class="pic" style="left:181px;top:66px;width:37px;height:46px">Picture Here</div>
</section>

<!-- 15 about us -->
<section class="slide c3 r5">
  <span class="rail-mark">Tovanta</span><span class="rail-line"></span><span class="rail-copy">Copyright © | All Rights Reserved</span><span class="rail-page">15</span>
  <div class="abs" style="left:23px;top:40px;font-size:10px;font-weight:500">About Us</div>
  <div class="abs" style="left:23px;top:57px;font-size:2.8px;color:var(--text)">No problem is too big or too small!<br><b style="color:var(--ink)">We're here to help.</b></div>
  <div class="abs copy" style="left:23px;top:69px;width:84px;font-size:2.8px">Lorem ipsum dolor sit amet, consectetur adipiscing elit, sed do eiusmod tempor incididunt ut labore et dolore magna aliqua. Lorem ipsum dolor sit amet, consectetur adipiscing elit, sed do eiusmod tempor incididunt ut labore et dolore magna aliqua. Ut enim ad minim veniam, quis nostrud exercitation ullamco laboris nisi ut aliquip.</div>
  <div class="pic" style="left:117px;top:0;width:110px;height:77px;align-items:flex-start;padding-top:38px">Picture Here</div>
  <div class="abs" style="left:117px;top:77px;width:110px;height:31px;background:var(--blue);border-radius:0 0 0 6px;padding:7px 7px;color:#fff;font-size:3.3px;font-weight:700;line-height:1.25">What you are seeking we have a solution, and if we do not, we know someone who will, this is our promise to you!</div>
</section>

<!-- 16 grey panel with pictures -->
<section class="slide c1 r6">
  <div class="abs" style="left:0;top:0;width:115px;height:128px;background:linear-gradient(90deg,#8b8b8b,#a3a3a3)"></div>
  <div class="abs" style="left:9px;top:28px;font-size:9px;font-weight:700;color:#fff;line-height:1">Here Add Your<br>Awesome Title</div>
  <div class="abs copy" style="left:9px;top:54px;width:84px;color:#fff">Lorem ipsum dolor sit amet, consectetur adipiscing elit, sed do eiusmod tempor incididunt ut labore et dolore magna aliqua. Lorem ipsum dolor sit amet, consectetur adipiscing elit, sed do eiusmod tempor incididunt ut labore et dolore magna aliqua. Ut enim ad minim veniam, quis nostrud exercitation ullamco laboris nisi ut aliquip.<br><br>Lorem ipsum dolor sit amet, consectetur adipiscing elit, sed do eiusmod tempor incididunt ut labore et dolore magna aliqua. Lorem ipsum dolor sit amet, consectetur adipiscing elit, sed do eiusmod tempor incididunt ut labore et dolore magna aliqua.</div>
  <div class="pic" style="left:95px;top:9px;width:53px;height:29px">Picture Here</div>
  <div class="pic" style="left:95px;top:48px;width:53px;height:29px">Picture Here</div>
  <div class="pic" style="left:95px;top:87px;width:53px;height:29px">Picture Here</div>
  <div class="abs" style="left:158px;top:13px;width:58px"><div class="label">Your Text Here</div><div class="copy">Lorem ipsum dolor sit amet, consectetur adipiscing elit, sed do eiusmod tempor incididunt ut labore et dolore magna aliqua.</div></div>
  <div class="abs" style="left:158px;top:54px;width:58px"><div class="label">Your Text Here</div><div class="copy">Lorem ipsum dolor sit amet, consectetur adipiscing elit, sed do eiusmod tempor incididunt ut labore et dolore magna aliqua.</div></div>
  <div class="abs" style="left:158px;top:93px;width:58px"><div class="label">Your Text Here</div><div class="copy">Lorem ipsum dolor sit amet, consectetur adipiscing elit, sed do eiusmod tempor incididunt ut labore et dolore magna aliqua.</div></div>
</section>

<!-- 17 three pictures -->
<section class="slide c2 r6">
  <span class="rail-mark">Tovanta</span><span class="rail-line"></span><span class="rail-copy">Copyright © | All Rights Reserved</span><span class="rail-page">17</span>
  <div class="h-title">Here Add Your Awesome Title</div><div class="h-sub">WRITE HERE A GREAT SUBTITLE</div><div class="h-rule"></div>
  <div class="abs" style="left:20px;top:41px;width:58px;text-align:center"><div class="label">Here Add Your Title</div><div class="copy">Lorem ipsum dolor sit amet, nec an dictas equidem appellantur, ut has commune accommodare.</div></div>
  <div class="pic" style="left:21px;top:65px;width:56px;height:63px">Picture Here</div>
  <div class="pic" style="left:87px;top:36px;width:55px;height:61px">Picture Here</div>
  <div class="abs" style="left:85px;top:102px;width:58px;text-align:center"><div class="label">Here Add Your Title</div><div class="copy">Lorem ipsum dolor sit amet, nec an dictas equidem appellantur, ut has commune accommodare.</div></div>
  <div class="abs" style="left:151px;top:41px;width:58px;text-align:center"><div class="label">Here Add Your Title</div><div class="copy">Lorem ipsum dolor sit amet, nec an dictas equidem appellantur, ut has commune accommodare.</div></div>
  <div class="pic" style="left:153px;top:65px;width:56px;height:63px">Picture Here</div>
</section>

<!-- 18 about us with ticks -->
<section class="slide c3 r6">
  <span class="rail-mark">Tovanta</span><span class="rail-line"></span><span class="rail-copy">Copyright © | All Rights Reserved</span><span class="rail-page">18</span>
  <div class="abs" style="left:21px;top:30px;font-size:9.5px;font-weight:500">About Us</div>
  <div class="abs" style="left:21px;top:43px;width:6px;height:.8px;background:var(--mid)"></div>
  <div class="abs copy" style="left:21px;top:47px;width:72px;font-weight:700;color:var(--ink)">Lorem ipsum dolor sit amet, consectetur adipiscing elit, sed do eiusmod tempor incididunt ut labore et dolore magna aliqua. Lorem ipsum dolor sit amet, consectetur adipiscing elit, sed do eiusmod tempor incididunt ut labore et dolore magna aliqua.</div>
  <svg class="abs" style="left:20px;top:73px" width="6" height="40" viewBox="0 0 6 40"><g fill="#3a6cf4"><circle cx="2.5" cy="3" r="2"/><circle cx="2.5" cy="19" r="2"/><circle cx="2.5" cy="35" r="2"/></g><g stroke="#fff" stroke-width=".6" fill="none"><path d="M1.6 3l.7.7 1.2-1.3"/><path d="M1.6 19l.7.7 1.2-1.3"/><path d="M1.6 35l.7.7 1.2-1.3"/></g></svg>
  <div class="abs copy" style="left:28px;top:72px;width:62px">Lorem ipsum dolor sit amet, consectetur adipiscing elit, sed do eiusmod tempor incididunt ut labore et dolore magna aliqua.</div>
  <div class="abs copy" style="left:28px;top:88px;width:62px">Lorem ipsum dolor sit amet, consectetur adipiscing elit, sed do eiusmod tempor incididunt ut labore et dolore magna aliqua.</div>
  <div class="abs copy" style="left:28px;top:104px;width:62px">Lorem ipsum dolor sit amet, consectetur adipiscing elit, sed do eiusmod tempor incididunt ut labore et dolore magna aliqua.</div>
  <div class="photo" role="img" aria-label="Two colleagues looking at a phone by a window" style="left:109px;top:0;width:118px;height:128px;background:linear-gradient(120deg,#8d8d8d,#d6d6d6 40%,#555 75%,#9a9a9a)"></div>
  <div class="mark" style="left:114px;top:46px;width:32px;height:32px;font-size:3.6px">Halvern<br>Group</div>
</section>

<!-- 19 table -->
<section class="slide c1 r7">
  <span class="rail-mark">Tovanta</span><span class="rail-line"></span><span class="rail-copy">Copyright © | All Rights Reserved</span><span class="rail-page">19</span>
  <div class="h-title" style="top:10px">Here Add Your Awesome Title</div><div class="h-sub" style="top:21px">WRITE HERE A GREAT SUBTITLE</div><div class="h-rule" style="top:25px"></div>
  <table class="grid-table" style="left:19px;top:40px;width:196px">
    <tr><th>Text</th><th>Text</th><th>Text</th><th>Text</th><th>Text</th><th>Text</th></tr>
    <tr><td>Data</td><td>Data</td><td>Data</td><td>Data</td><td>Data</td><td>Data</td></tr>
    <tr><td>Data</td><td>Data</td><td>Data</td><td>Data</td><td>Data</td><td>Data</td></tr>
    <tr><td>Data</td><td>Data</td><td>Data</td><td>Data</td><td>Data</td><td>Data</td></tr>
    <tr><td>Data</td><td>Data</td><td>Data</td><td>Data</td><td>Data</td><td>Data</td></tr>
    <tr class="hl"><td>Data</td><td>Data</td><td>Data</td><td>Data</td><td>Data</td><td>Data</td></tr>
  </table>
  <span class="icon-dot" style="left:23px;top:100px"></span><span class="icon-dot" style="left:130px;top:100px"></span>
  <div class="abs" style="left:40px;top:98px;width:68px"><div class="label">Project name</div><div class="copy">Lorem ipsum dolor sit amet, nec an dictas equidem appellantur, ut has commune accommodare. Mea illum, ludus solet idpro.</div></div>
  <div class="abs" style="left:147px;top:98px;width:68px"><div class="label">Project name</div><div class="copy">Lorem ipsum dolor sit amet, nec an dictas equidem appellantur, ut has commune accommodare. Mea illum, ludus solet idpro.</div></div>
</section>

<!-- 20 column comparison -->
<section class="slide c2 r7">
  <span class="rail-mark">Lumora</span><span class="rail-line"></span><span class="rail-copy">Copyright © | All Rights Reserved</span><span class="rail-page">20</span>
  <div class="h-title" style="top:15px">Here Add Your Awesome Title</div><div class="h-sub" style="top:26px">WRITE HERE A GREAT SUBTITLE</div><div class="h-rule" style="top:30px"></div>
  <div class="abs" style="left:23px;top:44px;width:188px;height:72px;display:grid;grid-template-columns:repeat(4,1fr);grid-template-rows:12px 30px 30px">
    <div style="background:var(--blue);color:#fff;font-size:3px;font-weight:700;display:flex;align-items:center;padding-left:4px">ADD YOUR TITLE</div>
    <div style="background:var(--blue);color:#fff;font-size:3px;font-weight:700;display:flex;align-items:center;padding-left:4px">ADD YOUR TITLE</div>
    <div style="background:var(--light);display:flex;align-items:center;justify-content:center"><span style="width:9px;height:9px;border-radius:50%;background:#fff;border:.5px solid var(--soft);font-size:1.5px;font-weight:700;display:flex;align-items:center;justify-content:center">Halvern</span></div>
    <div style="background:var(--blue);color:#fff;font-size:3px;font-weight:700;display:flex;align-items:center;padding-left:4px">ADD YOUR TITLE</div>
    <div style="background:var(--light);padding:3px 4px"><div style="font-size:2.8px;font-weight:700">Project name</div><div style="font-size:2px;line-height:1.4;color:#aaa">Lorem Ipsum is simply dummy text, a printer took a galley of type and made it.</div></div>
    <div style="background:var(--light);padding:3px 4px"><div style="font-size:2.8px;font-weight:700">Project name</div><div style="font-size:2px;line-height:1.4;color:#aaa">Lorem Ipsum is simply dummy text, a printer took a galley of type and made it.</div></div>
    <div style="background:#111;color:#fff;padding:3px 4px"><div style="font-size:2.8px;font-weight:700">Project name</div><div style="font-size:2px;line-height:1.4">Lorem Ipsum is simply dummy text, a printer took a galley of type and made it.</div></div>
    <div style="background:var(--light);padding:3px 4px"><div style="font-size:2.8px;font-weight:700">Project name</div><div style="font-size:2px;line-height:1.4;color:#aaa">Lorem Ipsum is simply dummy text, a printer took a galley of type and made it.</div></div>
    <div style="background:var(--light);padding:3px 4px"><div style="font-size:2.8px;font-weight:700">Project name</div><div style="font-size:2px;line-height:1.4;color:#aaa">Lorem Ipsum is simply dummy text, a printer took a galley of type and made it.</div></div>
    <div style="background:var(--light);padding:3px 4px"><div style="font-size:2.8px;font-weight:700">Project name</div><div style="font-size:2px;line-height:1.4;color:#aaa">Lorem Ipsum is simply dummy text, a printer took a galley of type and made it.</div></div>
    <div style="background:#111;color:#fff;padding:3px 4px"><div style="font-size:2.8px;font-weight:700">Project name</div><div style="font-size:2px;line-height:1.4">Lorem Ipsum is simply dummy text, a printer took a galley of type and made it.</div></div>
    <div style="background:var(--light);padding:3px 4px"><div style="font-size:2.8px;font-weight:700">Project name</div><div style="font-size:2px;line-height:1.4;color:#aaa">Lorem Ipsum is simply dummy text, a printer took a galley of type and made it.</div></div>
  </div>
</section>

<!-- 21 ring charts -->
<section class="slide c3 r7">
  <span class="rail-mark">Lumora</span><span class="rail-line"></span><span class="rail-copy">Copyright © | All Rights Reserved</span><span class="rail-page">21</span>
  <div class="h-title" style="top:15px">Here Add Your Awesome Title</div><div class="h-sub" style="top:26px">WRITE HERE A GREAT SUBTITLE</div><div class="h-rule" style="top:30px"></div>
  <div class="abs copy" style="left:22px;top:41px;width:190px;text-align:center;font-size:2.3px">Lorem Ipsum is simply placeholder text of the printing and typesetting industry. It has been the standard dummy text ever since the 1500s, when a printer took a galley of type and scrambled it to make a type specimen book. It has survived not only five centuries.</div>
  <svg class="abs" style="left:0;top:0" width="227" height="128" viewBox="0 0 227 128">
    <g fill="none" stroke-width="3.2">
      <circle cx="64" cy="77" r="15" stroke="#e3e3e3"/>
      <circle cx="64" cy="77" r="15" stroke="#9a9a9a" stroke-dasharray="47.1 94.2" transform="rotate(-90 64 77)"/>
      <circle cx="113" cy="77" r="15" stroke="#e3e3e3"/>
      <circle cx="113" cy="77" r="15" stroke="#555" stroke-dasharray="70.7 94.2" transform="rotate(-90 113 77)"/>
      <circle cx="161" cy="77" r="15" stroke="#e3e3e3"/>
      <circle cx="161" cy="77" r="15" stroke="#111" stroke-dasharray="37.7 94.2" transform="rotate(-90 161 77)"/>
    </g>
    <g font-family="Roboto, sans-serif" font-weight="700" font-size="9" text-anchor="middle" fill="#333">
      <text x="64" y="80.5">50%</text><text x="113" y="80.5">75%</text><text x="161" y="80.5">40%</text>
    </g>
  </svg>
  <div class="abs copy" style="left:47px;top:99px;width:34px;text-align:center;font-size:2.3px">Lorem ipsum dolor amet amet consectetur dolor</div>
  <div class="abs copy" style="left:96px;top:99px;width:34px;text-align:center;font-size:2.3px">Lorem ipsum dolor amet amet consectetur dolor</div>
  <div class="abs copy" style="left:144px;top:99px;width:34px;text-align:center;font-size:2.3px">Lorem ipsum dolor amet amet consectetur dolor</div>
</section>

<!-- 22 world map -->
<section class="slide c1 r8">
  <span class="rail-mark">Halvern</span><span class="rail-line"></span><span class="rail-copy">Copyright © | All Rights Reserved</span><span class="rail-page">22</span>
  <div class="photo" role="img" aria-label="World map with highlighted countries" style="left:18px;top:8px;width:200px;height:112px;border-radius:6px;background:radial-gradient(ellipse at 65% 35%,#b9bcc2,#eef2f8 60%,#fff)"></div>
  <svg class="abs" style="left:0;top:0" width="227" height="128" viewBox="0 0 227 128"><g fill="none" stroke="#3a6cf4" stroke-width=".4"><path d="M190 12 V40 H175"/><path d="M45 82 V70 H70"/><path d="M120 95 V70"/><path d="M170 108 V88 H180"/><path d="M196 66 H180"/></g></svg>
  <span class="tag" style="left:181px;top:8px">Text Here</span><div class="tag-copy" style="left:183px;top:13px">Lorem ipsum dolor sit amet, adipiscing elit integer pulvinar</div>
  <span class="tag" style="left:190px;top:62px">Text Here</span><div class="tag-copy" style="left:190px;top:67px">Lorem ipsum dolor sit amet, adipiscing elit integer pulvinar</div>
  <span class="tag" style="left:22px;top:80px">Text Here</span><div class="tag-copy" style="left:20px;top:85px">Lorem ipsum dolor sit amet, adipiscing elit integer pulvinar</div>
  <span class="tag" style="left:106px;top:95px">Text Here</span><div class="tag-copy" style="left:106px;top:100px">Lorem ipsum dolor sit amet, adipiscing elit integer pulvinar</div>
  <span class="tag" style="left:153px;top:108px">Text Here</span><div class="tag-copy" style="left:153px;top:113px">Lorem ipsum dolor sit amet, adipiscing elit integer pulvinar</div>
</section>

<!-- 23 circle of four -->
<section class="slide c2 r8">
  <span class="rail-mark">Tovanta</span><span class="rail-line"></span><span class="rail-copy">Copyright © | All Rights Reserved</span><span class="rail-page">23</span>
  <div class="h-title" style="top:10px">Here Add Your Awesome Title</div><div class="h-sub" style="top:21px">WRITE HERE A GREAT SUBTITLE</div><div class="h-rule" style="top:25px"></div>
  <svg class="abs" style="left:0;top:0" width="227" height="128" viewBox="0 0 227 128">
    <circle cx="114" cy="77" r="36" fill="#6e6e6e"/>
    <circle cx="114" cy="77" r="30" fill="none" stroke="#8a8a8a" stroke-width="5"/>
    <g stroke="#fff" stroke-width="1.2"><line x1="114" y1="41" x2="114" y2="113"/><line x1="78" y1="77" x2="150" y2="77"/></g>
    <g fill="none" stroke="#e6e6e6" stroke-width=".7"><circle cx="97" cy="58" r="3"/><circle cx="131" cy="58" r="3"/><circle cx="97" cy="96" r="3"/><circle cx="131" cy="96" r="3"/></g>
  </svg>
  <div class="mark dark" style="left:100px;top:63px;width:28px;height:28px;font-size:3.4px;border:1.5px solid #fff">Lumora</div>
  <div class="abs" style="left:22px;top:51px;width:58px;text-align:center"><div class="label">Your Contents Here</div><div class="copy">Lorem ipsum dolor sit amet, consectetur adipiscing elit, sed do eiusmod tempor incididunt.</div></div>
  <div class="abs" style="left:22px;top:89px;width:58px;text-align:center"><div class="label">Your Contents Here</div><div class="copy">Lorem ipsum dolor sit amet, consectetur adipiscing elit, sed do eiusmod tempor incididunt.</div></div>
  <div class="abs" style="left:153px;top:50px;width:58px"><div class="label">Your Contents Here</div><div class="copy">Lorem ipsum dolor sit amet, consectetur adipiscing elit, sed do eiusmod tempor incididunt.</div></div>
  <div class="abs" style="left:153px;top:88px;width:58px"><div class="label">Your Contents Here</div><div class="copy">Lorem ipsum dolor sit amet, consectetur adipiscing elit, sed do eiusmod tempor incididunt.</div></div>
</section>

<!-- 24 hub -->
<section class="slide c3 r8">
  <span class="rail-mark">Halvern</span><span class="rail-line"></span><span class="rail-copy">Copyright © | All Rights Reserved</span><span class="rail-page"></span>
  <div class="h-title" style="top:15px">Here Add Your Awesome Title</div><div class="h-sub" style="top:26px">WRITE HERE A GREAT SUBTITLE</div><div class="h-rule" style="top:30px"></div>
  <svg class="abs" style="left:0;top:0" width="227" height="128" viewBox="0 0 227 128">
    <g stroke="#d0d0d0" stroke-width=".5" fill="none"><path d="M77 45 L98 70"/><path d="M79 77 H96"/><path d="M77 112 L98 88"/><path d="M151 45 L130 70"/><path d="M150 77 H132"/><path d="M150 112 L130 88"/></g>
    <g fill="#c8c8c8"><circle cx="77" cy="45" r="1.6"/><circle cx="79" cy="77" r="1.6"/><circle cx="77" cy="112" r="1.6"/><circle cx="151" cy="45" r="1.6"/><circle cx="150" cy="77" r="1.6"/><circle cx="150" cy="112" r="1.6"/></g>
  </svg>
  <div class="mark" style="left:96px;top:62px;width:36px;height:36px;font-size:4px">Halvern<br>Group</div>
  <div class="abs" style="left:25px;top:43px;width:50px"><div class="label">Project Name</div><div class="copy">Lorem ipsum dolor sit amet, nec an dictas equidem appellantur, ut has commune.</div></div>
  <div class="abs" style="left:25px;top:71px;width:50px"><div class="label">Project Name</div><div class="copy">Lorem ipsum dolor sit amet, nec an dictas equidem appellantur.</div></div>
  <div class="abs" style="left:25px;top:100px;width:50px"><div class="label">Project Name</div><div class="copy">Lorem ipsum dolor sit amet, nec an dictas equidem appellantur.</div></div>
  <div class="abs" style="left:155px;top:43px;width:56px;text-align:right"><div class="label">Project Name</div><div class="copy">Lorem ipsum dolor sit amet, nec an dictas equidem appellantur, ut has commune.</div></div>
  <div class="abs" style="left:155px;top:71px;width:56px;text-align:right"><div class="label">Project Name</div><div class="copy">Lorem ipsum dolor sit amet, nec an dictas equidem appellantur.</div></div>
  <div class="abs" style="left:155px;top:100px;width:56px;text-align:right"><div class="label">Project Name</div><div class="copy">Lorem ipsum dolor sit amet, nec an dictas equidem appellantur.</div></div>
</section>

<!-- 25 closing -->
<section class="slide c1 r9">
  <div class="photo" role="img" aria-label="Softly faded office team background" style="inset:0;background:radial-gradient(ellipse at 50% 30%,#dcdcdc,#efefef 60%,#f6f6f6)"></div>
  <div class="mark" style="left:67px;top:46px;width:22px;height:22px;font-size:2.8px">Tovanta</div>
  <div class="mark" style="left:95px;top:32px;width:38px;height:38px;font-size:4px">Halvern<br>Group</div>
  <div class="mark dark" style="left:139px;top:46px;width:22px;height:22px;font-size:2.8px;border:1px solid #fff">Lumora</div>
  <div class="abs" style="left:0;right:0;top:84px;text-align:center;font-size:10px;font-weight:500">Thank You. Contact Us.</div>
  <svg class="abs" style="left:0;top:0" width="227" height="128" viewBox="0 0 227 128">
    <g fill="none" stroke="#3a6cf4" stroke-width=".5"><circle cx="30" cy="106" r="2"/><path d="M28 106h4M30 104c-1 1-1 3 0 4M30 104c1 1 1 3 0 4"/></g>
    <path d="M70 104.2a1.7 1.7 0 0 1 3.4 0c0 1.3-1.7 3.3-1.7 3.3s-1.7-2-1.7-3.3z" fill="#3a6cf4"/>
    <path d="M129 104.5c.4-.5 1-.6 1.3 0l.5.8c.1.3 0 .5-.2.7l-.3.2c.3.7.8 1.2 1.5 1.5l.2-.3c.2-.2.4-.3.7-.2l.8.5c.6.3.5.9 0 1.3-.9.8-4.8-2.5-4.5-4.5z" fill="#3a6cf4"/>
    <g fill="none" stroke="#3a6cf4" stroke-width=".5"><rect x="170" y="104.5" width="4" height="3"/><path d="M170 104.5l2 1.6 2-1.6"/></g>
  </svg>
  <div class="abs" style="left:35px;top:104.6px;font-size:2.4px">www.website.com</div>
  <div class="abs" style="left:75px;top:104.6px;font-size:2.4px">Here to write your Company adress</div>
  <div class="abs" style="left:136px;top:104.6px;font-size:2.4px">(555) 014-0199</div>
  <div class="abs" style="left:176px;top:104.6px;font-size:2.4px">info@website.com</div>
</section>

</main>
</body>
</html>
```